Webdesign für Onlineshop
Zielgruppe
Wir verkaufen in unserem Onlineshop alles zum Thema Wohnen mit dem Schwerpunkt Möbel. Die Hauptzielgruppe ist zwischen 25 und 45 Jahren.
Aufgabenstellung
Wir bevorzugen ein modernes, flaches und aufgeräumtes Design ähnlich wie velm.de / dorano88.de mit dem Fokus auf Preisaggressivität und Rabatte.
- Das Grundlayout muss so bleiben, wie es aktuell ist. Natürlich dürfen einzelne Elemente verschoben / versetzt werden.
- Im Header sollte Platz für eine kleine Werbefläche sein (ähnlich wie der konfigurierbare Kleiderschrank).
- Der Shop basiert auf Magento 1.9.
- Die Rabatte in den Produktdetailseiten müssen genauso aufgebaut sein
- Die Suche sollte in den Header platziert werden und nicht im Menü
- Ein SSL Logo soll im Header platziert weden
- Die Vorteile (Kostenloser Versand, Sicher einkaufen, Kauf auf Rechnung) sollen im Header erscheinen
- Das Design sollte responsive sein
Es wird nur das reine Design ohne Programmierung benötigt.

```html
<!DOCTYPE html>
<html lang="de">
<head>
<meta charset="utf-8">
<title>Wohnshop Startseite</title>
<link href="https://fonts.googleapis.com/css2?family=Roboto:wght@300;400;500;700&family=Open+Sans:wght@300;400&display=swap" rel="stylesheet">
<style>
:root{
  --bg:#ffffff;
  --text:#333333;
  --muted:#555555;
  --line:#e2e2e2;
  --sale:#b5115f;
  --teal:#3ea7b9;
  --green:#76a83a;
  --white:#ffffff;
}
*{box-sizing:border-box;margin:0;padding:0}
html,body{width:763px;height:1200px;overflow:hidden;background:var(--bg);font-family:"Roboto",sans-serif;color:var(--text)}
.page{position:relative;width:763px;height:1200px;overflow:hidden}
.hero-tile{position:absolute;top:21px;width:270px;height:188px;border-radius:3px;overflow:hidden}
.hero-tile--wardrobe{left:108px;background:linear-gradient(90deg,#7a5a45 0%,#d9b98c 30%,#f0d8c2 50%,#5b7fb3 75%,#c9c2b8 100%)}
.hero-tile--lounge{left:388px;background:linear-gradient(160deg,#2a2a2a 0%,#6f6f6f 40%,#b9bcbf 60%,#3a3a3a 100%)}
.hero-tile__title{position:absolute;left:23px;top:91px;color:var(--white);font-weight:700;font-size:16px;line-height:19.5px;text-shadow:0 1px 3px rgba(0,0,0,.45)}
.hero-tile--lounge .hero-tile__title{left:24px}
.btn-save{position:absolute;background:var(--green);color:var(--white);font-weight:500;font-size:12px;letter-spacing:.3px;display:flex;align-items:center;justify-content:center;width:106px;height:31px;border-radius:2px}
.hero-tile .btn-save{left:24px;top:139px}
.section-title{position:absolute;font-weight:300;font-size:21px;letter-spacing:.2px;text-transform:uppercase;color:#2b2b2b}
.slider-nav{position:absolute;display:flex;gap:8px}
.slider-nav__btn{width:30px;height:30px;border:1px solid #d8d8d8;border-radius:50%;display:flex;align-items:center;justify-content:center}
.product{position:absolute;width:130px}
.product__image{width:130px;height:89px}
.product__badge{position:absolute;left:-4px;top:-4px;width:34px;height:34px;border-radius:50%;background:var(--sale);color:var(--white);font-weight:500;font-size:10px;display:flex;align-items:center;justify-content:center}
.product__name{margin:12px 8px 0;font-weight:300;font-size:8.5px;line-height:10.5px;color:var(--muted);height:34px}
.product__old{margin:7px 8px 0;font-size:7px;text-decoration:line-through;color:#444}
.product__price{margin:1px 8px 0;font-size:13px;font-weight:400;color:var(--sale)}
.product__price--regular{color:var(--teal)}
.promo{position:absolute;left:108px;top:490px;width:549px;height:217px;border:1px solid var(--line);overflow:hidden;font-family:"Open Sans",sans-serif}
.promo__visual{position:absolute;right:0;top:0;width:330px;height:100%;background:linear-gradient(90deg,rgba(255,255,255,1) 0%,rgba(240,226,210,.6) 25%,#e9cfb5 50%,#cfe3f2 80%,#a9cdea 100%)}
.promo__title{position:absolute;left:34px;top:22px;font-size:20px;font-weight:400;color:#1f1f1f}
.promo__text{position:absolute;left:34px;top:52px;width:220px;font-size:9.5px;line-height:13.5px;font-weight:300;color:#555}
.promo__price{position:absolute;left:34px;top:100px;font-family:"Roboto",sans-serif;font-size:32px;font-weight:400;color:var(--teal)}
.promo .btn-save{left:35px;top:152px}
</style>
</head>
<body>
<div class="page">

  <div class="hero-tile hero-tile--wardrobe" role="img" aria-label="Frau vor einem offenen Kleiderschrank mit Kleidung">
    <div class="hero-tile__title">Ihr ganz persönlicher<br>Kleiderschrank</div>
    <div class="btn-save">40% GESPART</div>
  </div>
  <div class="hero-tile hero-tile--lounge" role="img" aria-label="Schwarze Ledersessel in einem Loft mit hohen Fenstern">
    <div class="hero-tile__title">Ihr ganz persönlicher<br>Kleiderschrank</div>
    <div class="btn-save">40% GESPART</div>
  </div>

  <h2 class="section-title" style="left:107px;top:240px">Unsere Topseller</h2>
  <div class="slider-nav" style="left:591px;top:242px">
    <div class="slider-nav__btn"><svg width="10" height="10" viewBox="0 0 10 10"><path d="M9 5H1M4.5 1.5 1 5l3.5 3.5" fill="none" stroke="#666" stroke-width="1"/></svg></div>
    <div class="slider-nav__btn"><svg width="10" height="10" viewBox="0 0 10 10"><path d="M1 5h8M5.5 1.5 9 5 5.5 8.5" fill="none" stroke="#666" stroke-width="1"/></svg></div>
  </div>

  <div class="product" style="left:108px;top:283px">
    <div class="product__image" role="img" aria-label="Schwarzes Boxspringbett im Schlafzimmer" style="background:linear-gradient(180deg,#e6e6e4 0%,#cfcfcf 50%,#3a3a3a 75%,#c9b24a 100%)"></div>
    <div class="product__badge">-36%</div>
    <p class="product__name">Wohnlandschaft, in Mikrofaser Vintage-Look braun</p>
    <p class="product__old">999,00 €</p>
    <p class="product__price">575,10 €</p>
  </div>
  <div class="product" style="left:248px;top:283px">
    <div class="product__image" role="img" aria-label="Schlafzimmer in Eiche-Dekor mit türkiser Bettwäsche" style="background:linear-gradient(180deg,#6e6257 0%,#a8977f 40%,#5fcad0 60%,#d8c29a 85%,#6a4a3a 100%)"></div>
    <div class="product__badge">-27%</div>
    <p class="product__name">Schlafzimmerkombination 4-tlg. in Eiche-Dekor mit Abs. in Lavagrau</p>
    <p class="product__old">999,00 €</p>
    <p class="product__price">575,10 €</p>
  </div>
  <div class="product" style="left:388px;top:283px">
    <div class="product__image" role="img" aria-label="Weißer Esstisch mit grauen Stühlen" style="background:linear-gradient(180deg,#a9cfd8 0%,#e9eef0 45%,#6b6e72 70%,#cfd2d4 100%)"></div>
    <div class="product__badge">-12%</div>
    <p class="product__name">Boxspringbett schwarz, Feinstrukturstoff</p>
    <p class="product__old">999,00 €</p>
    <p class="product__price">575,10 €</p>
  </div>
  <div class="product" style="left:527px;top:283px">
    <div class="product__image" role="img" aria-label="Braunes Sofa vor heller Wand" style="background:linear-gradient(180deg,#ebebeb 0%,#d8d8d8 50%,#6e4a38 70%,#4b2a20 100%)"></div>
    <div class="product__badge">-34%</div>
    <p class="product__name">Boxspringbett schwarz, Feinstrukturstoff</p>
    <p class="product__old">999,00 €</p>
    <p class="product__price">575,10 €</p>
  </div>

  <section class="promo">
    <div class="promo__visual" role="img" aria-label="Mutter und Tochter beim gemeinsamen Lesen"></div>
    <h3 class="promo__title">Kindgerecht und schön!</h3>
    <p class="promo__text">Entdecken Sie unsere kindgerechten Baby- und Kinderzimmer und zaubern Sie ihren Kleinen ein wundervolles Lächeln ins Gesicht!</p>
    <p class="promo__price">445,47 €</p>
    <div class="btn-save">40% GESPART</div>
  </section>

  <h2 class="section-title" style="left:103px;top:743px">Neu im Sortiment</h2>
  <div class="slider-nav" style="left:587px;top:745px">
    <div class="slider-nav__btn"><svg width="10" height="10" viewBox="0 0 10 10"><path d="M9 5H1M4.5 1.5 1 5l3.5 3.5" fill="none" stroke="#666" stroke-width="1"/></svg></div>
    <div class="slider-nav__btn"><svg width="10" height="10" viewBox="0 0 10 10"><path d="M1 5h8M5.5 1.5 9 5 5.5 8.5" fill="none" stroke="#666" stroke-width="1"/></svg></div>
  </div>

  <div class="product" style="left:104px;top:786px">
    <div class="product__image" role="img" aria-label="Weißes Bett mit roter Bettwäsche" style="background:linear-gradient(180deg,#e4e4e4 0%,#d0d0d0 40%,#b31a22 62%,#f1f1f1 85%,#9c9c9c 100%)"></div>
    <div class="product__badge">-36%</div>
    <p class="product__name">Wohnlandschaft, in Mikrofaser Vintage-Look braun</p>
    <p class="product__old">999,00 €</p>
    <p class="product__price">575,10 €</p>
  </div>
  <div class="product" style="left:244px;top:786px">
    <div class="product__image" role="img" aria-label="Helles Holzbett mit rosa Bettwäsche" style="background:linear-gradient(180deg,#9aa59a 0%,#d8d2c6 40%,#c99aa2 60%,#d6b98d 85%,#8c8c8c 100%)"></div>
    <p class="product__name">Boxspringbett schwarz, Feinstrukturstoff</p>
    <p class="product__old">999,00 €</p>
    <p class="product__price product__price--regular">575,10 €</p>
  </div>
  <div class="product" style="left:384px;top:786px">
    <div class="product__image" role="img" aria-label="Kleiderschrank aus Massivholz mit Spiegeltüren" style="background:linear-gradient(90deg,#8a5a2e 0%,#c48a4c 30%,#d9d4cc 50%,#c48a4c 70%,#8a5a2e 100%)"></div>
    <p class="product__name">Boxspringbett schwarz, Feinstrukturstoff</p>
    <p class="product__old">999,00 €</p>
    <p class="product__price product__price--regular">575,10 €</p>
  </div>
  <div class="product" style="left:523px;top:786px">
    <div class="product__image" role="img" aria-label="Schwarzes Boxspringbett im Schlafzimmer" style="background:linear-gradient(180deg,#e6e6e4 0%,#cfcfcf 50%,#3a3a3a 75%,#c9b24a 100%)"></div>
    <p class="product__name">Boxspringbett schwarz, Feinstrukturstoff</p>
    <p class="product__old">999,00 €</p>
    <p class="product__price product__price--regular">575,10 €</p>
  </div>

  <h2 class="section-title" style="left:102px;top:1000px">Beliebte Artikel</h2>
  <div class="slider-nav" style="left:586px;top:1002px">
    <div class="slider-nav__btn"><svg width="10" height="10" viewBox="0 0 10 10"><path d="M9 5H1M4.5 1.5 1 5l3.5 3.5" fill="none" stroke="#666" stroke-width="1"/></svg></div>
    <div class="slider-nav__btn"><svg width="10" height="10" viewBox="0 0 10 10"><path d="M1 5h8M5.5 1.5 9 5 5.5 8.5" fill="none" stroke="#666" stroke-width="1"/></svg></div>
  </div>

  <div class="product" style="left:103px;top:1043px">
    <div class="product__image" role="img" aria-label="Nachttisch aus Holz neben einem Bett" style="background:linear-gradient(135deg,#7b4d26 0%,#b78452 45%,#e8e3dc 70%,#5a5a5a 100%)"></div>
    <p class="product__name">Wohnlandschaft, in Mikrofaser Vintage-Look braun</p>
    <p class="product__old">999,00 €</p>
    <p class="product__price product__price--regular">575,10 €</p>
  </div>
  <div class="product" style="left:243px;top:1043px">
    <div class="product__image" role="img" aria-label="Graues Boxspringbett mit Decke" style="background:linear-gradient(180deg,#d8d8d8 0%,#bdbdbd 45%,#8a8a8a 65%,#c9c9c9 85%,#8a6a4a 100%)"></div>
    <p class="product__name">Boxspringbett schwarz, Feinstrukturstoff</p>
    <p class="product__old">999,00 €</p>
    <p class="product__price product__price--regular">575,10 €</p>
  </div>
  <div class="product" style="left:382px;top:1043px">
    <div class="product__image" role="img" aria-label="Schlafzimmer mit Kleiderschrank und türkiser Bettwäsche" style="background:linear-gradient(90deg,#4fc2c8 0%,#c7a779 35%,#4e4741 60%,#c7a779 85%,#e5e5e5 100%)"></div>
    <div class="product__badge">-36%</div>
    <p class="product__name">Boxspringbett schwarz, Feinstrukturstoff</p>
    <p class="product__old">999,00 €</p>
    <p class="product__price product__price--regular">575,10 €</p>
  </div>
  <div class="product" style="left:522px;top:1043px">
    <div class="product__image" role="img" aria-label="Weißer Nachttisch mit roter Bettdecke" style="background:linear-gradient(135deg,#3a3a3a 0%,#e9e9e9 40%,#f5f5f5 60%,#b8141f 85%,#9e9e9e 100%)"></div>
    <p class="product__name">Boxspringbett schwarz, Feinstrukturstoff</p>
    <p class="product__old">999,00 €</p>
    <p class="product__price product__price--regular">575,10 €</p>
  </div>

</div>
</body>
</html>
```